Need a design for Loan Site with new age design

We need a design for our site www.fernpivot.in , we deal with different verticals like home loan, personal loan, loan against property and business loans. Feel free to get in touch if you have any questions.

I have like the concept of the drop down on the eye level where consumer is able to select the product they wish and continue with the form https://www.tallowcrest.com/ . They are in the same line of business as we are.

Here are few more designs which i personally like just to get idea about the taste

https://plumweatherly.com/
http://vexlar.com/partners

Industry/Entity Type

Loan

Number of Pages Required

2 page

Colors
34a7d7
add136
faa54b
fbee3e

Requirements
Must have
• I have like the concept of the drop down on the eye level where consumer is able to select the product they wish and continue with the form https://www.tallowcrest.com/ . They are in the same line of business as we are.
• Here are few more designs which i personally like just to get idea about the taste
• https://plumweatherly.com/
• http://vexlar.com/partners

```html
<!DOCTYPE html>
<html lang="en">
<head>
<meta charset="utf-8">
<title>Fern Pivot – Loans</title>
<link href="https://fonts.googleapis.com/css2?family=Open+Sans:wght@400;600;700&display=swap" rel="stylesheet">
<style>
:root{
  --green:#add136;
  --blue:#34a7d7;
  --orange:#faa54b;
  --yellow:#fbee3e;
  --ink:#333;
  --footer:#3d3d3d;
  --footer-deep:#323232;
  --white:#fff;
}
*{box-sizing:border-box;margin:0;padding:0}
html,body{width:932px;height:1200px;overflow:hidden}
body{font-family:'Open Sans',sans-serif;color:var(--ink);background:#fff;position:relative}
.abs{position:absolute}

/* header */
.site-header{position:absolute;top:0;left:0;width:932px;height:76px;border-top:2px solid var(--blue);background:#fff}
.brand{position:absolute;left:74px;top:26px;display:flex;align-items:center;gap:8px;font-size:17px;font-weight:600;color:#1c5c9a}
.brand .mark{width:14px;height:14px;background:var(--blue)}
.nav{position:absolute;left:239px;top:-2px;display:flex;height:78px}
.nav a{width:98px;height:78px;display:flex;align-items:center;justify-content:center;color:#fff;font-size:12px;font-weight:600;text-decoration:none}
.nav .g{background:var(--green)}.nav .b{background:#4cb1dc}.nav .o{background:var(--orange)}.nav .y{background:var(--yellow)}
.search{position:absolute;left:852px;top:32px}

/* hero */
.hero{position:absolute;top:76px;left:0;width:932px;height:324px;background:radial-gradient(ellipse at 50% 45%,#4a423a 0%,#332d28 60%,#26221f 100%)}
.hero h1{position:absolute;top:124px;width:100%;text-align:center;color:#fff;font-size:20.5px;font-weight:600}
.hero p{position:absolute;top:164px;width:100%;text-align:center;color:#fff;font-size:14.5px}
.select{position:absolute;top:218px;height:32px;width:188px;background:#fff;font-size:9.5px;color:#777;padding:0 10px;display:flex;align-items:center;justify-content:space-between}
.btn-search{position:absolute;top:218px;left:597px;width:127px;height:32px;background:var(--blue);color:#fff;font-size:12.5px;font-weight:600;display:flex;align-items:center;justify-content:center}
.hero .arrow{position:absolute;top:155px}

/* perks */
.perks{position:absolute;top:400px;left:0;width:932px;height:54px;background:var(--green);display:flex;align-items:center;padding-left:76px;gap:0}
.perk{display:flex;align-items:center;gap:10px;color:#fff;font-size:12px;font-weight:600;margin-right:38px}

/* partners */
.partner{position:absolute;top:484px;width:147px;height:66px;border:1px solid #e6e6e6;display:flex;align-items:center;justify-content:center;gap:7px;font-size:14px;font-weight:600;color:#555}
.partner .dot{width:12px;height:12px;border-radius:50%;background:#ccc}
.rule{position:absolute;top:577px;left:0;width:932px;height:2px;background:#f2f2f2}

/* features */
.feature-art{position:absolute;left:76px;top:598px;width:313px;height:224px;background:linear-gradient(135deg,#f4e3c2 0%,#e8b867 45%,#a8324a 100%)}
.divider{position:absolute;left:463px;top:600px;width:1px;height:220px;background:linear-gradient(#fff,#ddd,#fff)}
.features h2{position:absolute;left:521px;top:604px;font-size:20px;font-weight:600;color:var(--green)}
.features ul{list-style:none;position:absolute;left:524px;top:652px;font-size:11.5px;color:#444}
.features li{height:33px;display:flex;gap:12px}
.features li::before{content:"»";color:#555}
.btn-join{position:absolute;left:526px;top:789px;width:88px;height:31px;background:var(--blue);color:#fff;font-size:15px;font-weight:600;display:flex;align-items:center;justify-content:center;border-radius:2px}

/* tiles */
.tiles{position:absolute;top:860px;left:0;display:flex;width:932px}
.tile{width:133.15px;height:92px;display:flex;flex-direction:column;align-items:center;justify-content:flex-end;padding-bottom:14px;color:#fff;font-size:11px;font-weight:600;gap:6px}
.tile svg{width:46px;height:42px}

/* footer */
.site-footer{position:absolute;top:952px;left:0;width:932px;height:191px;background:var(--footer);color:#fff}
.fcol{position:absolute;top:28px}
.fcol h3{font-size:12.5px;font-weight:400;margin-bottom:12px}
.fcol li{list-style:none;font-size:9.5px;height:21.3px}
.fcol li::before{content:"»";margin-right:8px}
.contact li::before{content:none}
.contact li{display:flex;gap:12px;height:auto;margin-bottom:12px;line-height:1.8;font-size:9.5px}
.social{display:flex;gap:10px;margin-top:4px}
.social span{width:28px;height:28px;border:2px solid #fff;border-radius:50%}
.email{margin-top:22px;width:132px;height:26px;background:#fff;color:#999;font-size:9.5px;display:flex;align-items:center;justify-content:space-between;padding:0 8px}
.legal{position:absolute;top:1143px;left:0;width:932px;height:57px;background:var(--footer-deep);color:#fff;font-size:9.5px;display:flex;align-items:center;justify-content:center;gap:6px}
</style>
</head>
<body>

<header class="site-header">
  <div class="brand"><span class="mark"></span>Fern Pivot</div>
  <nav class="nav">
    <a class="g">Home</a><a class="b">Who we are</a><a class="o">Services</a><a class="y">Blog</a><a class="g">Career</a><a class="b">Reach us</a>
  </nav>
  <svg class="search" width="12" height="12" viewBox="0 0 12 12"><circle cx="5" cy="5" r="3.6" fill="none" stroke="#34a7d7" stroke-width="1.8"/><line x1="7.6" y1="7.6" x2="10.5" y2="10.5" stroke="#34a7d7" stroke-width="1.8"/></svg>
</header>

<section class="hero" role="img" aria-label="Desk photo with hands, charts, coins and a calculator around a meeting table">
  <svg class="arrow" style="left:33px" width="10" height="16" viewBox="0 0 10 16"><path d="M8 2 2 8l6 6" fill="none" stroke="#fff" stroke-width="2"/></svg>
  <svg class="arrow" style="left:885px" width="10" height="16" viewBox="0 0 10 16"><path d="M2 2l6 6-6 6" fill="none" stroke="#fff" stroke-width="2"/></svg>
  <h1>Looking for a Secured Or Unsecured Loan ?</h1>
  <p>We will help you get best interest rate</p>
  <div class="select" style="left:213px">I would like to <svg width="8" height="5"><path d="M1 1l3 3 3-3" fill="none" stroke="#777"/></svg></div>
  <div class="select" style="left:405px">Select a Product <svg width="8" height="5"><path d="M1 1l3 3 3-3" fill="none" stroke="#777"/></svg></div>
  <div class="btn-search">Search Here</div>
</section>

<div class="perks">
  <div class="perk"><svg width="30" height="30" viewBox="0 0 30 30" fill="none" stroke="#fff" stroke-width="1.8"><path d="M15 3 25 7v8c0 6-5 10-10 12C10 25 5 21 5 15V7z"/><circle cx="15" cy="13" r="3"/><path d="M10 21c1-3 9-3 10 0"/></svg>85+ Banks &amp; Insurers</div>
  <div class="perk"><svg width="30" height="30" viewBox="0 0 30 30" fill="none" stroke="#fff" stroke-width="1.8"><circle cx="15" cy="15" r="11"/><path d="M15 8v7h5"/></svg>Fast Approvals</div>
  <div class="perk"><svg width="30" height="30" viewBox="0 0 30 30" fill="#fff"><circle cx="15" cy="9" r="6"/><path d="M4 28c0-8 5-11 11-11s11 3 11 11z"/></svg>80,00,000+ Happy Customers</div>
  <div class="perk"><svg width="30" height="30" viewBox="0 0 30 30" fill="none" stroke="#fff" stroke-width="1.8"><path d="M15 2l3 4 5-1 1 5 4 3-3 4 1 5-5 1-2 4-4-2-4 2-2-4-5-1 1-5-3-4 4-3 1-5 5 1z"/><line x1="11" y1="19" x2="19" y2="11"/><circle cx="11.5" cy="11.5" r="1.5"/><circle cx="18.5" cy="18.5" r="1.5"/></svg>Exclusive Offers &amp; Rates</div>
</div>

<svg class="abs" style="left:34px;top:504px" width="14" height="26" viewBox="0 0 14 26"><path d="M12 1 2 13l10 12" fill="none" stroke="#bbb" stroke-width="1.5"/></svg>
<div class="partner" style="left:76px"><span class="dot"></span>Quorvel</div>
<div class="partner" style="left:235px"><span class="dot"></span>Brisa Capital</div>
<div class="partner" style="left:393px"><span class="dot"></span>Glad Patron</div>
<div class="partner" style="left:551px"><span class="dot"></span>Tidewell Energy</div>
<div class="partner" style="left:709px"><span class="dot"></span>Larkmoor Property</div>
<svg class="abs" style="left:884px;top:504px" width="14" height="26" viewBox="0 0 14 26"><path d="M2 1l10 12L2 25" fill="none" stroke="#bbb" stroke-width="1.5"/></svg>
<div class="rule"></div>

<section class="features">
  <div class="feature-art" role="img" aria-label="Illustration of a smiling customer at a laptop giving a thumbs-up while an agent holds up a document"></div>
  <div class="divider"></div>
  <h2>Fern Pivot Features</h2>
  <ul>
    <li>Easy Documentation</li>
    <li>Compare Quote from all major financial institutions</li>
    <li>Doorstep Deliveries</li>
    <li>Get Approval within 7 business days</li>
  </ul>
  <div class="btn-join">Join Us</div>
</section>

<div class="tiles">
  <div class="tile" style="background:var(--green)"><svg viewBox="0 0 46 42" fill="#fff"><path d="M23 4 4 20h5v18h10V27h8v11h10V20h5z"/></svg>Home Loan</div>
  <div class="tile" style="background:#4cb1dc"><svg viewBox="0 0 46 42" fill="#fff"><path d="M10 8h26l5 13v12h-5v4h-6v-4H16v4h-6v-4H5V21z"/><rect x="13" y="11" width="20" height="9" fill="#4cb1dc"/><circle cx="12" cy="27" r="3" fill="#4cb1dc"/><circle cx="34" cy="27" r="3" fill="#4cb1dc"/></svg>Car Loan</div>
  <div class="tile" style="background:var(--orange)"><svg viewBox="0 0 46 42" fill="none" stroke="#fff" stroke-width="2.4"><path d="M10 9h26l5 12v11H5V21z"/><path d="M8 20h30"/><circle cx="12" cy="26" r="2.5"/><circle cx="34" cy="26" r="2.5"/><path d="M8 32v5h6v-5M32 32v5h6v-5"/></svg>Used Car Loan</div>
  <div class="tile" style="background:var(--yellow)"><svg viewBox="0 0 46 42" fill="none" stroke="#fff" stroke-width="2.4"><circle cx="23" cy="13" r="8"/><path d="M8 39c0-10 7-14 15-14s15 4 15 14z"/></svg>Personal Loan</div>
  <div class="tile" style="background:var(--green)"><svg viewBox="0 0 46 42" fill="none" stroke="#fff" stroke-width="2.4"><rect x="4" y="14" width="30" height="22" rx="2"/><path d="M16 14l4-10 24 8-6 16"/><rect x="9" y="22" width="8" height="5"/></svg>Credit Loan</div>
  <div class="tile" style="background:#4cb1dc"><svg viewBox="0 0 46 42" fill="#fff"><path d="M6 8l18-4 4 8H10z"/><rect x="4" y="12" width="38" height="26" rx="3"/><rect x="14" y="19" width="24" height="14" rx="2" fill="#4cb1dc"/><circle cx="21" cy="29" r="2"/><circle cx="25" cy="29" r="2"/></svg>Debit Loan</div>
  <div class="tile" style="background:var(--orange)"><svg viewBox="0 0 46 42" fill="none" stroke="#fff" stroke-width="2.4"><path d="M4 14l9-8 8 5h6l8-5 9 8-7 6-10 11-4 3-5-5-4-4z"/><path d="M21 11l-6 6 4 3 6-5 10 9"/></svg>Business Loan</div>
</div>

<footer class="site-footer">
  <div class="fcol" style="left:75px"><h3>Home loan</h3><ul><li>Northbay Loan</li><li>Crestline Loan</li><li>Harlow Loan</li><li>Meridian Loan</li><li>Orrin Loan</li></ul></div>
  <div class="fcol" style="left:189px"><h3>Personal loan</h3><ul><li>Northbay Loan</li><li>Crestline Loan</li><li>Harlow Loan</li><li>Meridian Loan</li><li>Orrin Loan</li></ul></div>
  <div class="fcol" style="left:307px"><h3>Property loan</h3><ul><li>Northbay Loan</li><li>Crestline Loan</li><li>Harlow Loan</li><li>Meridian Loan</li><li>Orrin Loan</li></ul></div>
  <div class="fcol" style="left:421px"><h3>Business loan</h3><ul><li>Northbay Loan</li><li>Crestline Loan</li><li>Harlow Loan</li><li>Meridian Loan</li><li>Orrin Loan</li></ul></div>
  <div class="fcol contact" style="left:540px"><h3>Contact us</h3><ul>
    <li><svg width="13" height="12" viewBox="0 0 13 12" fill="#fff"><path d="M6.5 1 0 6.5h2V11h3.5V8h2v3H11V6.5h2z"/></svg><span>5120 Harwick Ln. | Fairmont<br>KS 60014</span></li>
    <li><svg width="13" height="14" viewBox="0 0 13 14" fill="none" stroke="#fff" stroke-width="1.5"><rect x="3" y="1" width="7" height="12" rx="1"/></svg><span>Call Us : (555)010-2468</span></li>
    <li><svg width="13" height="12" viewBox="0 0 13 12" fill="none" stroke="#fff" stroke-width="1.3"><rect x="1" y="2" width="11" height="8"/><path d="M1 2l5.5 4L12 2"/></svg><span>info@fernpivot.in</span></li>
  </ul></div>
  <div class="fcol" style="left:716px"><h3>Connect us with</h3>
    <div class="social" aria-label="Social network links"><span></span><span></span><span></span><span></span></div>
    <div class="email">Email <span>»</span></div>
  </div>
</footer>
<div class="legal"><svg width="11" height="11" viewBox="0 0 11 11" fill="none" stroke="#fff"><circle cx="5.5" cy="5.5" r="4.8"/><path d="M7.3 4a2.3 2.3 0 1 0 0 3"/></svg>Companyname 2016 . All Rights Reserved</div>

</body>
</html>
```